Modern Website Design for an Online Travel Agency.. Design Only!!

Hi there!

We are building an website for our travel agency that caters to tourists traveling to the Cayman Islands. We provide travel information and take bookings for various tours available here.

We need designs for 8 different web page layouts. You can see the layout specifications in two attached documents. We do not have a need for the coding to be done. This will simply act as a blueprint for our developer to build from.

The important pages are the 'Home Page' 'checkout page' and the ‘Checkout Page’ (Page 1 & 10 in the PDF ‘Website Layout’)

The MOST important page is ‘Tour Search Page’ (page 6)

If you intend on only submitting one page design, please submit a design for page 6. Be aware though, the more of these 3 page designs you submit, the more likely we are to move forward with you!

At this stage, we are simply looking to develop the most aesthetic website design layout possible.

- The website should be colour coordinated with the logo. You can most certainly use other colours if you feel they complement the overall design of the website well.

- Everything must be laid out in an EXTREMELY simple & ‘easy to navigate’ way. The key is simplicity & Functionality. There is no need for messy or elaborate graphics.

- The website MUST have a VERY clean and modern appearance.

- We want the main background to be white, but you can use light grey in places to compliment or add dimension if you feel necessary.

- We will appreciate a good use of shadows and especially a good use of icons. (You can see examples of icons we have already designed, we are definitely open to new icon design concepts too)

- We will reward imagination and original thinking! Essentially we want a website with a creative touch and unique design elements, whilst maintaining that clean and simple layout.

- Most importantly!! - Paying attention to the small details will be highly rewarded (A well balanced and seamless use of fonts, colours, dimensions, shadowing, positioning, etc)

If you have any questions, please don’t hesitate to ask.

We’re excited to see your design submissions!

Thank you!!

You can find all the support documents and content at: https://www.filevorra.net/sh/9qm2rtwplexan7c/QQBmTtZnPdLsWEGxvvaJpLmRw?dl=0

Target Market(s)

Tourists

Industry/Entity Type

Travel

Number of Pages Required

5+ page

Font styles to use
Sans Serif

Colors

Designer to choose colors to be used in the design.

Requirements
Must have
• Must be very clean and modern.
• Must be simple and bold
• Must be color coordinated in a way that makes sense
• White background
Nice to have
• Good use of shadows and Icons
Should not have
• Over use of messy graphics
• And design layout which is not right angled (using anything but vertical or horizontal for the edges in the design)

```html
<!DOCTYPE html>
<html lang="en">
<head>
<meta charset="utf-8">
<title>Isle Harbor – Travel Concierges</title>
<link href="https://fonts.googleapis.com/css2?family=Poppins:wght@400;500;600;700&family=Montserrat:wght@400;500;600;700&display=swap" rel="stylesheet">
<style>
:root{
  --green:#8dc63f;
  --blue:#1f6fc5;
  --ink:#222326;
  --text:#4a4a4a;
  --light:#f4f4f4;
  --footer:#25262a;
  --white:#ffffff;
}
*{margin:0;padding:0;box-sizing:border-box}
html,body{width:1200px;height:2240px;overflow:hidden;background:var(--white)}
body{position:relative;font-family:'Montserrat',sans-serif;color:var(--text)}
.abs{position:absolute}
.hero{left:0;top:0;width:1200px;height:490px;background:linear-gradient(180deg,#1f5fb8 0%,#3a8ad6 35%,#5f9a4a 70%,#d8cfae 100%)}
.hero-tail{left:0;top:490px;width:439px;height:87px;background:linear-gradient(180deg,#d8cfae,#c9c1a3)}
.brand{font-family:'Poppins',sans-serif;font-weight:600;display:flex;align-items:center;gap:8px}
.brand .mark{width:30px;height:30px;border-radius:50%}
.topbar-brand{left:94px;top:40px;font-size:25px;color:var(--white)}
.topbar-brand .mark{background:var(--white)}
.nav{left:378px;top:51px;width:530px;display:flex;justify-content:space-between;font-size:11.5px;color:var(--white);white-space:nowrap}
.nav a{color:inherit;text-decoration:none}
.nav a.active{font-weight:700}
.dest-drop{left:1019px;top:11px;font-family:'Poppins',sans-serif;font-size:12px;font-weight:500;color:var(--white)}
.btn-outline{border:1px solid var(--white);color:var(--white);font-family:'Poppins',sans-serif;font-weight:600;font-size:12px;display:flex;align-items:center;justify-content:center;gap:6px}
.usd{left:934px;top:43px;width:82px;height:31px}
.login{left:1024px;top:43px;width:82px;height:31px}
.hero-rule{left:101px;top:130px;width:1px;height:279px;background:rgba(255,255,255,.7)}
.social{left:95px;top:436px;display:flex;flex-direction:column;gap:12px}
.social span{width:12px;height:12px;background:var(--white);border-radius:2px}
.hero-kicker{left:0;width:1200px;top:234px;text-align:center;font-family:'Poppins',sans-serif;font-weight:600;font-size:29px;color:var(--white)}
.hero-title{left:0;width:1200px;top:258px;text-align:center;font-family:'Poppins',sans-serif;font-weight:700;font-size:72px;color:var(--white);letter-spacing:-.5px}
.know-more{left:533px;top:346px;width:134px;height:44px;border:2px solid var(--white);color:var(--white);font-family:'Poppins',sans-serif;font-weight:600;font-size:13px;display:flex;align-items:center;justify-content:center}
.slide-next{left:1073px;top:231px;width:31px;height:30px;background:var(--green)}
.slide-prev{left:1075px;top:267px;width:29px;height:29px;border:1.5px solid var(--white)}
.welcome{left:290px;top:518px;font-family:'Poppins',sans-serif;font-weight:600;font-size:17px;color:var(--white)}
.welcome-line{left:407px;top:531px;width:64px;height:1.5px;background:var(--blue)}
.intro-title{left:480px;top:508px;font-family:'Poppins',sans-serif;font-weight:600;font-size:34px;color:var(--ink)}
.intro-copy{left:480px;top:563px;width:622px;font-size:11px;line-height:16.5px}
.intro-copy p+p{margin-top:16px}
.btn-green{background:var(--green);color:var(--white);font-family:'Montserrat',sans-serif;font-weight:700;letter-spacing:1.6px;display:flex;align-items:center;justify-content:center;text-align:center}
.read-more{left:480px;top:723px;width:123px;height:40px;font-size:11px}
.sea{left:665px;top:830px;width:442px;height:583px;background:linear-gradient(180deg,#0d3d9a 0%,#2a6fc9 35%,#3fb7a5 55%,#3cc8b0 75%,#2aa79b 100%)}
.process{left:94px;top:887px;width:698px;height:470px;background:var(--light);box-shadow:0 4px 14px rgba(0,0,0,.12)}
.process h2{position:absolute;left:0;width:100%;top:26px;text-align:center;font-family:'Poppins',sans-serif;font-weight:600;font-size:33px;color:var(--ink)}
.step{position:absolute;top:89px;width:150px;height:345px;text-align:center}
.step .badge{position:absolute;left:4px;top:0;width:36px;height:30px;border-radius:50%;border-bottom:2px solid var(--blue);color:var(--blue);font-family:'Poppins',sans-serif;font-weight:500;font-size:15px;line-height:28px;background:var(--white)}
.step .art{margin:0 auto;width:130px;height:146px;border-radius:8px;background:linear-gradient(160deg,#e4eef8,#dcefc4)}
.step h3{margin-top:18px;font-family:'Poppins',sans-serif;font-weight:500;font-size:13px;line-height:17px;color:var(--ink)}
.step p{margin-top:6px;font-size:9.6px;line-height:14.3px}
.step .btn-green{position:absolute;left:20px;top:307px;width:109px;height:33px;font-size:9px;line-height:11px;letter-spacing:1.2px}
.photo{top:1496px;width:251px;height:343px}
.photo-brac{left:94px;background:linear-gradient(180deg,#dfe7ef 0%,#8fb2cc 35%,#2a6ea0 70%,#1b4f86 100%)}
.photo-grand{left:371px;background:linear-gradient(180deg,#5d88c9 0%,#2f6bb3 30%,#1c3f8a 60%,#13307a 100%)}
.photo-little{left:648px;background:linear-gradient(180deg,#c9d9e8 0%,#4b7a4c 25%,#49c8c2 55%,#3bd0c4 100%)}
.caption{top:1853px;width:251px;text-align:center;font-family:'Poppins',sans-serif;font-weight:500;font-size:14px;color:var(--ink)}
.dest-card{left:856px;top:1550px;width:251px;height:308px;background:var(--light);box-shadow:0 4px 14px rgba(0,0,0,.1)}
.dest-line{left:838px;top:1671px;width:36px;height:1.5px;background:var(--blue)}
.dest-title{left:880px;top:1648px;font-family:'Poppins',sans-serif;font-weight:600;font-size:33px;color:var(--ink)}
.dest-btn{left:920px;top:1708px;width:123px;height:39px;font-size:11px}
.arrows{left:1024px;top:1495px}
.footer{left:0;top:1911px;width:1200px;height:329px;background:var(--footer)}
.footer-brand{left:0;width:1200px;top:1950px;justify-content:center;font-size:40px;color:var(--blue)}
.footer-brand .mark{width:44px;height:44px;border-radius:6px;background:var(--green)}
.contact{top:2052px;display:flex;align-items:center;gap:14px;font-size:19px;color:var(--white);font-weight:400}
.contact .ico{width:48px;height:48px}
.contact-divider{top:2035px;width:1px;height:100px;background:rgba(255,255,255,.15)}
.foot-rule{left:0;top:2176px;width:1200px;height:1px;background:rgba(255,255,255,.15)}
.copyright{left:94px;top:2199px;font-size:11px;color:#cfcfcf}
.copyright b{font-weight:400;color:var(--green)}
.legal{left:886px;top:2199px;font-size:11px;color:#cfcfcf;word-spacing:2px}
</style>
</head>
<body>

<div class="abs hero" role="img" aria-label="Photo of friends jumping joyfully on a sunny beach with palm trees"></div>
<div class="abs hero-tail" role="img" aria-label="Sandy beach continuation of the hero photo"></div>

<div class="abs brand topbar-brand"><span class="mark"></span>IsleHarbor</div>
<nav class="abs nav">
  <a class="active">Home</a><a>Discover Cayman</a><a>Thing to Do</a><a>My Trip Planner</a><a>Map</a><a>Tours</a><a>Contact Us</a>
</nav>
<div class="abs dest-drop">Destinations ⌄</div>
<div class="abs btn-outline usd">USD$</div>
<div class="abs btn-outline login">
  <svg width="14" height="14" viewBox="0 0 14 14" fill="none" stroke="#fff" stroke-width="1.2"><path d="M5 1h8v12H5M1 7h8M6 4l3 3-3 3"/></svg>Login
</div>

<div class="abs hero-rule"></div>
<div class="abs social"><span></span><span></span><span></span><span></span></div>

<div class="abs hero-kicker">We are Proud Travel concierges of the</div>
<div class="abs hero-title">Cayman Islands</div>
<div class="abs know-more">KNOW MORE</div>

<div class="abs slide-next"><svg width="31" height="30" fill="none" stroke="#fff" stroke-width="1.3"><path d="M-12 15h32M15 10l5 5"/></svg></div>
<div class="abs slide-prev"><svg width="29" height="29" fill="none" stroke="#fff" stroke-width="1.3"><path d="M8 14h32M13 19l-5-5"/></svg></div>

<div class="abs welcome">Welcome to</div>
<div class="abs welcome-line"></div>
<h1 class="abs intro-title">Isle Harbor</h1>
<div class="abs intro-copy">
  <p>We are proud travel concierges of the Cayman Islands! We help thousands of tourists visiting Cayman every year arrange vacation getaway catered to their exact needs. With a wealth of local knowledge, we help you avoid unreliable tour operators and find those local hidden gems. Here you can research everything you need to be fully prepared for your travels and also view the complete range of activities available.</p>
  <p>Once you’re ready to move forward, we’ll help you fine tune your itinerary and continue to make all the booking arrangements on your behalf. All of our services are 100% FREE with No Hidden Costs. Meaning you pay exactly the same prices as though you were booking directly with the tour operators yourself.</p>
</div>
<div class="abs btn-green read-more">READ MORE</div>

<div class="abs sea" role="img" aria-label="Photo of turquoise sea with a palm-lined shore"></div>

<section class="abs process">
  <h2>Our 4 Step Process</h2>
  <div class="step" style="left:19px">
    <span class="badge">01</span>
    <div class="art" role="img" aria-label="Illustration of a relaxed traveller choosing activities"></div>
    <h3>Choose Your<br>Favorite Activities</h3>
    <p>Keep the fun of planning and easily budget your entire trip. We’ll deal with the hard work and handle all your booking arrangements.</p>
    <div class="btn-green">FIND YOUR FUN!</div>
  </div>
  <div class="step" style="left:188px">
    <span class="badge">02</span>
    <div class="art" role="img" aria-label="Illustration of a traveller using an online trip planner"></div>
    <h3>Use Our Online<br>Travel Planner</h3>
    <p>Organize your favorite activities on our user-friendly trip planner to effortlessly design your perfect vacation. Use our planner to easily budget your entire trip!</p>
    <div class="btn-green">GO TO TRIP PLANNER</div>
  </div>
  <div class="step" style="left:353px">
    <span class="badge">03</span>
    <div class="art" role="img" aria-label="Illustration of travellers arranging a vacation package"></div>
    <h3>We Make All<br>The Arrangements</h3>
    <p>Fill out our simple form and we’ll use our local expertise to design your ideal vacation package. Best of all, our services are 100% FREE!</p>
    <div class="btn-green">GO TO TRIP PLANNER</div>
  </div>
  <div class="step" style="left:522px">
    <span class="badge">04</span>
    <div class="art" role="img" aria-label="Illustration of a traveller relaxing on vacation"></div>
    <h3>Relax and Enjoy<br>Your Vacation</h3>
    <p>Consider us your guardian angels during your stay. We continue to offer support throughout your trip, so you can truly enjoy your vacation, stress free!</p>
    <div class="btn-green">FIND YOUR TRAVEL ANGEL!</div>
  </div>
</section>

<div class="abs photo photo-brac" role="img" aria-label="Aerial photo of Cayman Brac island"></div>
<div class="abs photo photo-grand" role="img" aria-label="Aerial photo of Grand Cayman coastline"></div>
<div class="abs photo photo-little" role="img" aria-label="Photo of Little Cayman shallow turquoise water"></div>
<div class="abs caption" style="left:94px">Cayman Brac</div>
<div class="abs caption" style="left:371px">Grand Cayman</div>
<div class="abs caption" style="left:648px;top:1857px">Little Cayaman</div>

<div class="abs dest-card"></div>
<div class="abs dest-line"></div>
<h2 class="abs dest-title">Destinations</h2>
<div class="abs btn-green dest-btn">KONW MORE</div>
<svg class="abs arrows" width="82" height="16" fill="none" stroke="#333" stroke-width="1.3">
  <path d="M1 11h36M1 11l6 5M46 6h36M82 6l-6-5"/>
</svg>

<footer class="abs footer"></footer>
<div class="abs brand footer-brand"><span class="mark"></span>IsleHarbor</div>

<div class="abs contact" style="left:158px">
  <svg class="ico" viewBox="0 0 48 48" fill="none" stroke="#8dc63f" stroke-width="1.3"><path d="M24 2l22 22-22 22L2 24z"/><path d="M18 17l3-1 3 5-2 2q2 4 6 6l2-2 5 3-1 3q-9 1-16-16z"/></svg>
  <span>01-555-014-220</span>
</div>
<div class="abs contact-divider" style="left:406px"></div>
<div class="abs contact" style="left:481px">
  <svg class="ico" viewBox="0 0 48 48" fill="none" stroke="#8dc63f" stroke-width="1.3"><path d="M24 2l22 22-22 22L2 24z"/><path d="M14 18h20v13H14zM14 18l10 8 10-8"/></svg>
  <span>hello@isleharbor</span>
</div>
<div class="abs contact-divider" style="left:772px"></div>
<div class="abs contact" style="left:836px;line-height:22px">
  <svg class="ico" viewBox="0 0 48 48" fill="none" stroke="#8dc63f" stroke-width="1.3"><path d="M24 2l22 22-22 22L2 24z"/><path d="M24 34s-7-8-7-13a7 7 0 0114 0c0 5-7 13-7 13z"/><circle cx="24" cy="21" r="2.5"/></svg>
  <span>45 BC, making it<br>over 2000</span>
</div>

<div class="abs foot-rule"></div>
<div class="abs copyright">© 2019 <b>Isle Harbor</b>. All Right Reserved.</div>
<div class="abs legal">Privacy Policy &nbsp; | &nbsp; Term and Condition</div>

</body>
</html>
```